Website - Tides Of Bloom

We are catalysts of change in people's lives.
We work with individuals and professionals to bring about instant substantial & transforming change in their lives.
We provide one-on-one lifestyle coaching by an experienced practitioner.
Our existing website is www.tidesofbloom.biz & this site contains our the basis for the content of our desired new project, so please examine this carefully.
We require a professional and captivating website that will instantly impress, engage invite our readers to click & invest their lives.
Our services do not come cheap, but are second to none.
Our website must be contemporary whilst reflecting indisputable class & ultra-confidence in the success of our work.
Target Market(s)
Those who seek to want to change in their lives. Those aged primarily between 30 and 50 years of age, male or female.
Industry/Entity Type
Work
Look and feel

```html
<!DOCTYPE html>
<html lang="en">
<head>
<meta charset="utf-8">
<title>Tides Of Bloom</title>
<link href="https://fonts.googleapis.com/css2?family=Montserrat:wght@300;400;500;600;700&family=Crimson+Text:ital,wght@0,400;0,600;1,400&family=Barlow+Semi+Condensed:wght@700&display=swap" rel="stylesheet">
<style>
:root{
  --black:#050505;
  --hero-deep:#1e2d5e;
  --hero-mid:#34497f;
  --hero-light:#5d73a9;
  --cyan:#35c3e0;
  --orange:#f29a1d;
  --lime:#8cc63f;
  --green:#5fbf2a;
  --red:#e8262a;
  --ink:#1b1b1b;
  --body:#3a3a3a;
  --page:#f1f1f1;
  --white:#fff;
  --grey-text:#9a9a9a;
  --beige-a:#ebe2d7;
  --beige-b:#cfbfad;
}
*{margin:0;padding:0;box-sizing:border-box}
html,body{width:1200px;height:2268px;overflow:hidden}
body{position:relative;background:var(--page);font-family:"Crimson Text",Georgia,serif;color:var(--body)}
.abs{position:absolute}

/* header */
.site-header{left:0;top:0;width:1200px;height:136px;background:var(--black)}
.brand{left:151px;top:40px;display:flex;align-items:center;gap:14px}
.brand-mark{width:56px;height:56px;border-radius:50%;background:var(--orange)}
.brand-name{font-family:"Montserrat",sans-serif;font-weight:600;font-size:32px;color:var(--white);line-height:1}
.social-top{left:832px;top:19px;display:flex;gap:9px}
.social-top span{width:30px;height:30px;border-radius:4px;background:#3b5ea8;display:block}
.social-top span:nth-child(4){background:#d34836}
.social-top span:nth-child(5){background:#d2281e}
.social-top span:nth-child(6){background:#f08a24}
.call{left:832px;top:62px;color:#d7d7d7;font-size:24px;line-height:1}
.call-number{left:832px;top:88px;color:var(--green);font-size:32px;line-height:1}

/* nav */
.main-nav{left:0;top:136px;width:1200px;height:47px;background:linear-gradient(#1a1a1a,#050505);border-top:1px solid #2a2a2a}
.main-nav ul{list-style:none;display:flex;height:100%;padding-left:134px}
.main-nav li{font-family:"Montserrat",sans-serif;font-size:14px;color:var(--white);display:flex;align-items:center;padding:0 16px;border-right:1px solid #2c2c2c;height:100%}
.main-nav li:last-child{border-right:none}

/* hero */
.hero{left:0;top:183px;width:1200px;height:569px;background:linear-gradient(90deg,var(--hero-mid) 0%,var(--hero-light) 40%,var(--hero-mid) 70%,var(--hero-deep) 100%);overflow:hidden}
.hero-photo{left:540px;top:0;width:660px;height:569px;background:linear-gradient(90deg,rgba(60,80,130,0) 0%,rgba(72,92,140,.55) 40%,rgba(58,76,122,.6) 100%)}
.hero-points{left:145px;top:82px}
.point{position:relative;padding-left:38px;margin-bottom:32px}
.point svg{position:absolute;left:0;top:6px}
.point-lead{font-family:"Montserrat",sans-serif;font-size:24px;color:var(--white);line-height:1.2}
.point-key{font-family:"Montserrat",sans-serif;font-weight:700;font-size:32px;line-height:1.15;letter-spacing:.5px}
.key-cyan{color:var(--cyan)}.key-orange{color:var(--orange)}.key-lime{color:var(--lime)}
.hero-slogan{left:146px;bottom:-16px;font-family:"Barlow Semi Condensed",sans-serif;font-weight:700;font-size:112px;letter-spacing:1px;color:rgba(255,255,255,.3);line-height:1}

/* content */
.content{left:142px;top:752px;width:916px;height:1053px;background:var(--white)}
.feature{top:29px;width:265px;height:242px;background:var(--white);box-shadow:0 0 6px rgba(0,0,0,.18)}
.feature-head{height:70px;background:linear-gradient(#fafafa,#e6e6e6);padding:16px 20px 0}
.feature-kicker{font-family:"Montserrat",sans-serif;font-size:18px;color:var(--ink);line-height:1.1}
.feature-title{font-family:"Montserrat",sans-serif;font-weight:700;font-size:22px;color:var(--ink);line-height:1.1}
.feature p{padding:14px 20px 0;font-size:15px;line-height:1.36;color:var(--body)}
.feature-link{position:absolute;left:18px;bottom:22px;height:16px;padding:0 22px 0 12px;background:var(--red);color:var(--white);font-family:"Montserrat",sans-serif;font-size:9px;font-weight:600;letter-spacing:1px;line-height:16px;clip-path:polygon(6px 0,100% 0,calc(100% - 6px) 100%,0 100%)}

.welcome-small{left:26px;top:318px;font-family:"Montserrat",sans-serif;font-weight:300;font-size:36px;color:#8d8d8d;line-height:1}
.welcome-big{left:26px;top:358px;font-family:"Montserrat",sans-serif;font-weight:600;font-size:36px;color:var(--ink);line-height:1}
.intro{left:26px;top:428px;width:630px}
.intro .lede{font-size:24px;color:var(--ink);line-height:1.6}
.intro p{font-size:15.5px;line-height:1.38;margin-top:16px}
.intro .lede + .lede{margin-top:0}

.portrait{left:671px;top:284px;width:293px;height:769px;background:linear-gradient(180deg,rgba(232,232,232,0) 0%,#e8e8e8 18%,#dedede 100%)}

.testimonials{left:-10px;top:771px;width:920px;height:229px;background:linear-gradient(100deg,var(--beige-a),var(--beige-b));box-shadow:0 4px 8px rgba(0,0,0,.15)}
.testimonials-kicker{left:36px;top:20px;font-family:"Montserrat",sans-serif;font-size:18px;color:var(--ink);line-height:1.1}
.testimonials-title{left:36px;top:40px;font-family:"Montserrat",sans-serif;font-weight:600;font-size:24px;color:var(--ink);line-height:1.1}
.avatar{left:48px;top:93px;width:72px;height:72px;border-radius:50%;background:#b9a797;border:4px solid var(--white);box-shadow:0 0 4px rgba(0,0,0,.2)}
.quote{left:148px;top:86px;width:530px;font-size:15.5px;line-height:1.36;color:var(--body)}
.quote-author{left:148px;top:168px;font-size:14px;font-style:italic;color:var(--body)}

/* footer */
.site-footer{left:0;top:1805px;width:1200px;height:391px;background:var(--black)}
.contact-item{top:80px;height:66px;display:flex;align-items:center;gap:20px;color:var(--grey-text)}
.contact-item .text{font-size:14px;line-height:1.55}
.contact-item .phone{font-family:"Montserrat",sans-serif;font-size:20px}
.slash{top:58px;width:2px;height:120px;background:#2a2a2a;transform:rotate(20deg)}
.footer-rule{left:104px;top:215px;width:992px;height:1px;background:#222}
.social-title{left:0;top:252px;width:1200px;text-align:center;font-family:"Montserrat",sans-serif;font-weight:400;font-size:27px;color:#e3e3e3;letter-spacing:1px;line-height:1.2}
.social-row{left:450px;top:308px;width:300px;display:flex;justify-content:center;gap:10px}
.social-row span{width:42px;height:42px;border-radius:50%;background:#3a3a3a;display:block}
.bottom-bar{left:0;top:2196px;width:1200px;height:72px;background:#161616;font-size:12px;color:#8a8a8a}
.copyright{left:140px;top:26px}
.legal{right:140px;top:26px}
</style>
</head>
<body>

<header class="site-header abs">
  <div class="brand abs"><span class="brand-mark"></span><span class="brand-name">Tides Of Bloom</span></div>
  <div class="social-top abs"><span></span><span></span><span></span><span></span><span></span><span></span></div>
  <div class="call abs">Call Ethan today on</div>
  <div class="call-number abs">+61 02 5550 1742</div>
</header>

<nav class="main-nav abs">
  <ul>
    <li>HOME</li><li>ABOUT</li><li>BUSINESS</li><li>INDIVIDUAL</li><li>CLIENT SERVICES</li><li>EVENTS</li><li>SUCCESS STORIES</li><li>CONTACT</li>
  </ul>
</nav>

<section class="hero abs">
  <div class="hero-photo abs" role="img" aria-label="Photo of a smiling coach in front of a cheering crowd"></div>
  <div class="hero-points abs">
    <div class="point">
      <svg width="28" height="18" viewBox="0 0 28 18"><path d="M2 16 C6 6 14 4 22 6 L18 1 M22 6 L17 10" fill="none" stroke="#fff" stroke-width="3" stroke-linecap="round"/></svg>
      <div class="point-lead">More choices about your behaviours and</div>
      <div class="point-key key-cyan">EMOTIONS</div>
    </div>
    <div class="point">
      <svg width="28" height="18" viewBox="0 0 28 18"><path d="M2 16 C6 6 14 4 22 6 L18 1 M22 6 L17 10" fill="none" stroke="#fff" stroke-width="3" stroke-linecap="round"/></svg>
      <div class="point-lead">Improve your relationships and the ways</div>
      <div class="point-key key-orange">YOU COMMUNICATE</div>
    </div>
    <div class="point">
      <svg width="28" height="18" viewBox="0 0 28 18"><path d="M2 16 C6 6 14 4 22 6 L18 1 M22 6 L17 10" fill="none" stroke="#fff" stroke-width="3" stroke-linecap="round"/></svg>
      <div class="point-lead">Create better results through becoming</div>
      <div class="point-key key-lime">A GREATER THINKER</div>
    </div>
  </div>
  <div class="hero-slogan abs">CHANGE IS YOURS</div>
</section>

<main class="content abs">
  <article class="feature abs" style="left:26px">
    <div class="feature-head"><div class="feature-kicker">INTERNATIONALLY</div><div class="feature-title">ACCREDITED</div></div>
    <p>Lorem Ipsum is simply dummy text of the printing and typesetting industry. Lorem Ipsum has been the industry's standard dummy text ever since the 1500s.</p>
    <span class="feature-link">VIEW DETAILS ➔</span>
  </article>
  <article class="feature abs" style="left:327px">
    <div class="feature-head"><div class="feature-kicker">CONVENIENT AND</div><div class="feature-title">AFFORDABLE</div></div>
    <p>Lorem Ipsum is simply dummy text of the printing and typesetting industry. Lorem Ipsum has been the industry's standard dummy text ever since the 1500s.</p>
    <span class="feature-link">VIEW DETAILS ➔</span>
  </article>
  <article class="feature abs" style="left:625px">
    <div class="feature-head"><div class="feature-kicker">PRATICAL COACHING</div><div class="feature-title">TRAINING</div></div>
    <p>Lorem Ipsum is simply dummy text of the printing and typesetting industry. Lorem Ipsum has been the industry's standard dummy text ever since the 1500s.</p>
    <span class="feature-link">VIEW DETAILS ➔</span>
  </article>

  <h2 class="welcome-small abs">Welcome to</h2>
  <h1 class="welcome-big abs">TIDES OF BLOOM</h1>
  <div class="intro abs">
    <p class="lede">Not a lifelong project or years of therapy.</p>
    <p class="lede">Change begins today with our Master Practitioner.</p>
    <p>Our clients experience their desired instant &amp; permanent transformation, emerging from our consultations ready to take on their world from a vastly different paradigm</p>
    <p>At Tides Of Bloom, our Master Practitioner will inspire you, shifting your perspective &amp; facilitating your mind with the freedom to realise your dreams</p>
    <p>Join Marcus Hale, Adrian Cole, R.M. Ashdown, Theo Marsh, Owen Pryce, Delia Raymond and hundreds of thousands of others who are achieving the life changing, consistent results you are dreaming of now.</p>
  </div>

  <section class="testimonials abs">
    <div class="testimonials-kicker abs">CLIENT'S</div>
    <h3 class="testimonials-title abs">TESTIMONIALS</h3>
    <div class="avatar abs" role="img" aria-label="Client photo"></div>
    <p class="quote abs">Lorem Ipsum is simply dummy text of the printing and typesetting industry. Lorem Ipsum has been the industry's standard dummy text ever since the 1500s. It has survived not only five centuries.</p>
    <div class="quote-author abs">- Lena Varga</div>
  </section>

  <div class="portrait abs" role="img" aria-label="Photo of a smiling client in a white blouse"></div>
</main>

<footer class="site-footer abs">
  <div class="contact-item abs" style="left:140px">
    <svg width="32" height="44" viewBox="0 0 32 44"><path d="M16 0C7 0 0 7 0 16c0 12 16 28 16 28s16-16 16-28C32 7 25 0 16 0z" fill="#e8262a"/><circle cx="16" cy="16" r="6" fill="#050505"/></svg>
    <div class="text">Tides of Bloom<br>101 Street no,<br>Country, 0012348</div>
  </div>
  <div class="slash abs" style="left:412px"></div>
  <div class="contact-item abs" style="left:466px">
    <svg width="40" height="36" viewBox="0 0 40 36"><path d="M4 10 C4 2 36 2 36 10 L30 14 L28 9 L12 9 L10 14 Z" fill="#e8262a"/><path d="M8 16 L32 16 L36 34 L4 34 Z" fill="#e8262a"/><circle cx="20" cy="25" r="5" fill="#050505"/></svg>
    <div class="phone">+61 02 5550 1742</div>
  </div>
  <div class="slash abs" style="left:798px"></div>
  <div class="contact-item abs" style="left:846px">
    <svg width="40" height="34" viewBox="0 0 40 34"><path d="M0 12 L20 0 L40 12 L40 34 L0 34 Z" fill="#e8262a"/><path d="M2 14 L20 26 L38 14" fill="none" stroke="#050505" stroke-width="3"/></svg>
    <div class="text">info@tidesofbloom.biz</div>
  </div>
  <div class="footer-rule abs"></div>
  <h3 class="social-title abs">LET'S BE SOCIAL</h3>
  <div class="social-row abs"><span></span><span></span><span></span><span></span><span></span><span></span></div>
</footer>

<div class="bottom-bar abs">
  <div class="copyright abs">© 2013 Tides Of Bloom, Ltd. All Rights Reserved.</div>
  <div class="legal abs">Privacy Policy &nbsp;|&nbsp; Sitemap</div>
</div>

</body>
</html>
```